Dane Morrow films- wedding and event films company website. DESKTOP AND MOBILE

We need a website for a high-end wedding and event film production company. Looking for a very modern and elegant design. my old website is www.danemorrowfilms.example

I like the "white/black/rose gold" color scheme of my logo.

really looking for a sleek modern design the breaths professional and artistic.

Target Market(s)

wedding and event films.

Industry/Entity Type

Film Production

Number of Pages Required

5+ page

Colors

Designer to choose colors to be used in the design.

Requirements
Must have
• website name will be www.danemorrowfilms.example
• tagline is "CINEMATIC STORIES ABOUT YOU"
• sections: HOME, CONTACT, ABOUT, FILMS, BLOG
• You can see my old website at danemorrowfilms.example
• Website about section:
• Dane Morrow Films was Established with the basis of truly cinematic and artistic films in mind. Dane and his team routinely travel the globe documenting weddings and events for high profile clients and discerning couples. Dane was born and raised in Maui Hawaii and has a unique approach to his films that embody the essence of a Hollywood film. Dane has spent the last 10 years traveling the world documenting corporate events and weddings with multiple Award winning production companies. In 2017 Dane decided to establish his own brand “Dane Morrow films” that will take everything he has learned with his past experiences and push it to the next level. Aside from his personal achievements, Dane is extremely passionate about his craft and always looks forward to handcrafting beautiful wedding/event films for his clients. The style of work is non-traditional and the day of filming is extremely unobtrusive (as we are looking for natural-candid/ raw emotions).
• If you are looking for the best price in town, we are probably not the best option, but if you’re looking for the best quality and peace of mind on your wedding day, then you’re in the right place. Dane Morrow Films is a boutique studio that only accepts a limited number of assignments per year. Inquire early to ensure availability.
• LINKS TO VIMEO VIDEOS THAT WILL BE IN THE "FILMS' SECTION.
• BRENT FILM TRAILER - https://clipvault.example/508114362
• BRENT FEATURE FILM - https://clipvault.example/617392048
• JUNE AND ROB'S WEDDING - https://clipvault.example/724958160
• DRONE DEMO REEL - https://clipvault.example/841576203
• WEDDING INDUSTRY EVENT PARTY - https://clipvault.example/962304817/a8d3e7b21c
• images that you can use on site are here: https://brigittolsenimages.proofbox.example/gallery/nora&felix/
• password is: meadow

```html
<!DOCTYPE html>
<html lang="en">
<head>
<meta charset="utf-8">
<title>Dane Morrow Films</title>
<link rel="stylesheet" href="https://fonts.googleapis.com/css2?family=Raleway:wght@400;500&family=Fira+Sans+Extra+Condensed:ital,wght@1,800&display=swap">
<style>
  :root {
    --ink: #000000;
    --paper: #ffffff;
    --gold: #c3a35a;
  }
  * { margin: 0; padding: 0; box-sizing: border-box; }
  html, body { width: 1200px; height: 818px; overflow: hidden; background: var(--ink); }
  body { font-family: "Raleway", sans-serif; color: var(--paper); }
  .page { position: relative; width: 1200px; height: 818px; }
  .backdrop { position: absolute; inset: 0; }

  .main-nav { position: absolute; left: 87px; top: 13px; display: flex; gap: 15px; }
  .main-nav a { color: var(--paper); text-decoration: none; font-size: 13px; }
  .book-cta { position: absolute; right: 86px; top: 14px; font-size: 13px; color: var(--paper); text-decoration: none; }

  .brand { position: absolute; left: 420px; top: 96px; width: 360px; text-align: center; color: var(--paper); font-weight: 400; white-space: nowrap; }
  .brand-name { display: block; font-size: 22px; letter-spacing: 3px; line-height: 22px; }
  .brand-sub { display: block; font-size: 11px; letter-spacing: 6px; line-height: 11px; margin-top: 4px; }

  .thumb-column { position: absolute; top: 156px; width: 167px; height: 372px; background: var(--ink); }
  .thumb-column.left { left: 153px; }
  .thumb-column.right { left: 888px; }
  .thumb { position: absolute; left: 17px; width: 131px; height: 91px; border-radius: 8px; }
  .thumb.t1 { top: 21px; } .thumb.t2 { top: 142px; } .thumb.t3 { top: 261px; }

  .headline { position: absolute; left: 388px; top: 218px; width: 426px; text-align: center;
    font-family: "Fira Sans Extra Condensed", sans-serif; font-style: italic; font-weight: 800;
    font-size: 33px; color: var(--ink); letter-spacing: 0.5px; }
  .headline .hd { font-size: 38px; letter-spacing: 2px; }

  .feature-film { position: absolute; left: 388px; top: 267px; width: 426px; height: 222px;
    background: var(--ink); border-radius: 20px; padding: 7px; }
  .feature-still { width: 100%; height: 100%; border-radius: 14px;
    background: linear-gradient(180deg, #e8e1d6 0%, #cfc6b8 45%, #8d8377 100%); position: relative; }
  .play { position: absolute; left: 183px; top: 79px; }

  .contact { position: absolute; left: 400px; top: 592px; width: 400px; text-align: center; font-size: 11px; line-height: 20px; }
  .testimonial { position: absolute; left: 250px; top: 658px; width: 700px; text-align: center; font-size: 13px; line-height: 15px; }
  .testimonial cite { display: block; font-style: normal; color: var(--gold); }
</style>
</head>
<body>
<div class="page">
  <svg class="backdrop" width="1200" height="818" viewBox="0 0 1200 818" aria-hidden="true">
    <path fill="var(--paper)" d="M78,103 C110,75 160,64 214,64 C380,64 480,158 600,158 C720,158 820,64 986,64 C1040,64 1090,75 1121,103 L1121,600 C1090,625 1040,640 986,640 C820,640 720,547 600,547 C480,547 380,640 214,640 C160,640 110,625 78,600 Z"/>
    <path fill="var(--gold)" d="M78,48 C300,30 470,148 600,148 C730,148 900,30 1121,48 L1121,71 C900,55 730,154 600,154 C470,154 300,55 78,71 Z"/>
    <path fill="var(--gold)" d="M78,633 C300,648 470,551 600,551 C730,551 900,648 1121,633 L1121,658 C900,672 730,556 600,556 C470,556 300,672 78,658 Z"/>
  </svg>

  <nav class="main-nav">
    <a href="#">HOME</a><a href="#">THEATRE</a><a href="#">ABOUT</a><a href="#">CONTACT</a>
  </nav>
  <a class="book-cta" href="#">book your wedding or event film now!</a>

  <div class="brand">
    <span class="brand-name">DANE MORROW</span>
    <span class="brand-sub">FILMS</span>
  </div>

  <div class="thumb-column left">
    <div class="thumb t1" role="img" aria-label="Curling ocean wave at the shore" style="background:linear-gradient(160deg,#7fa8c4,#3d6b52 60%,#a6a05a)"></div>
    <div class="thumb t2" role="img" aria-label="Pink lotus flower among lily pads" style="background:linear-gradient(160deg,#4c7a2e,#c45a9a 50%,#b5a52b)"></div>
    <div class="thumb t3" role="img" aria-label="Smiling couple embracing" style="background:linear-gradient(160deg,#d9dde2,#b89a86 55%,#2c2f3a)"></div>
  </div>

  <div class="thumb-column right">
    <div class="thumb t1" role="img" aria-label="Bride and groom silhouetted at sunset" style="background:linear-gradient(180deg,#6c6c8a,#e2a17a 50%,#3a2a2a)"></div>
    <div class="thumb t2" role="img" aria-label="Rocky beach with trees under blue sky" style="background:linear-gradient(180deg,#6b9fd6,#4d6a3a 45%,#c9b79a 70%,#3a3a3a)"></div>
    <div class="thumb t3" role="img" aria-label="Pink heart balloons at a party" style="background:linear-gradient(160deg,#f5b3e6,#e05ccf 55%,#c04bb0)"></div>
  </div>

  <h1 class="headline">FULL SERVICE <span class="hd">HD</span></h1>

  <div class="feature-film">
    <div class="feature-still" role="img" aria-label="Bride and groom dancing on a rocky coastline at dusk">
      <svg class="play" width="58" height="58" viewBox="0 0 58 58" aria-hidden="true">
        <circle cx="29" cy="29" r="27" fill="none" stroke="var(--paper)" stroke-width="2.5"/>
        <path d="M22,16 L42,29 L22,42 Z" fill="var(--paper)"/>
      </svg>
    </div>
  </div>

  <div class="contact">
    <p>(808) 555-0143</p>
    <p>dane@danemorrowfilms.example</p>
  </div>

  <blockquote class="testimonial">
    <p>“Dane really is one of the best film makers in Hawaii, great work Dane! We loved the film!”</p>
    <cite>— Lena Harwick</cite>
  </blockquote>
</div>
</body>
</html>
```